Business Cards/ Stationery for Dental Office
Willow Gate Dental
Business Cards/ Stationery for Dental Office - Health
Creative Brief
Simple
Celia R. Marlow, DDS
2715 Pelton Ridge Franklin, Tn 37069
willowgatedental@mailvane.com
www.willowgatedental.com
Please also add a facebook icon. Link is www.facebook/willowgatedental Also, for the business cards I would like one business card with logo on one side and all pertinent info on the other side. Then another business card (for older people who might actually want an appointment card) that on the back side says Appointment at the top. Then says Name:, Date:, Time:

```html
<!DOCTYPE html>
<html lang="en">
<head>
<meta charset="utf-8">
<title>Willow Gate Dental – Stationery</title>
<link rel="stylesheet" href="https://fonts.googleapis.com/css2?family=Cormorant+Garamond:wght@500;600;700&display=swap">
<style>
  :root{
    --stage:#4b4b4b;
    --brand-grey:#8c8c8c;
    --brand-grey-dark:#7e7e7e;
    --accent:#d9e05a;
    --paper:#ffffff;
    --ink-light:#f2f2f2;
    --ink-dark:#555555;
    --rule:#c9c9c9;
  }
  *{box-sizing:border-box;margin:0;padding:0}
  html,body{width:1200px;height:547px;overflow:hidden;background:var(--stage)}
  body{position:relative;font-family:"Cormorant Garamond",Georgia,serif;color:var(--ink-light)}
  .piece{position:absolute;overflow:hidden}

  .card{width:144px;height:78px;border-radius:4px;background:var(--brand-grey)}
  .card--info{left:91px;top:173px}
  .card--front{left:257px;top:173px}
  .card--back{left:91px;top:271px}
  .card--appointment{left:257px;top:271px;background:var(--paper);color:var(--ink-dark)}

  .brand{display:flex;flex-direction:column;align-items:center;text-align:center;font-weight:600;color:var(--ink-light);line-height:1}
  .brand__dot{width:7px;height:7px;border-radius:50%;background:var(--ink-light);margin-bottom:3px}
  .brand__name{font-size:12px;letter-spacing:.5px}
  .brand--lg .brand__name{font-size:15px}
  .brand--sm .brand__name{font-size:9px}

  .card--info .brand{position:absolute;left:8px;top:18px;width:62px}
  .card--info .brand__name{font-size:10px}
  .card--info .contact{position:absolute;left:76px;top:24px;font-size:4.6px;line-height:1.5;color:var(--ink-light)}
  .card--front .brand{position:absolute;left:0;right:0;top:20px}
  .card--back .brand{position:absolute;left:0;right:0;top:10px}
  .card--back .doctor{position:absolute;left:0;right:0;top:48px;text-align:center;font-size:6px;font-weight:700;color:var(--accent)}
  .card--back .contact{position:absolute;left:0;right:0;top:57px;text-align:center;font-size:4.4px;line-height:1.4}

  .appointment{padding:9px 10px;font-size:6px;font-weight:700}
  .appointment h2{font-size:7px;font-weight:700;margin-bottom:6px}
  .appointment .field{display:flex;align-items:flex-end;gap:3px;margin-bottom:7px}
  .appointment .field span{flex:1;border-bottom:.6px solid var(--rule);height:5px}

  .letterhead{left:458px;top:38px;width:329px;height:468px;background:var(--paper)}
  .letterhead__head{height:62px;background:var(--brand-grey);border-bottom:3px solid var(--accent);position:relative}
  .letterhead__head .brand{position:absolute;left:16px;top:14px;width:70px}
  .letterhead__contact{position:absolute;left:232px;top:8px;font-size:4.6px;line-height:1.7}
  .letterhead__foot{position:absolute;left:0;right:0;bottom:0;height:12px;background:var(--brand-grey)}

  .contact li{list-style:none;display:flex;align-items:center;gap:3px}
  .contact .ico{width:4px;height:4px;flex:none;background:var(--ink-light)}
  .contact .ico--round{border-radius:50%}

  .envelope{left:809px;top:202px;width:348px;height:163px;background:var(--paper)}
  .envelope__head{height:46px;background:var(--brand-grey);border-bottom:3px solid var(--accent);position:relative}
  .envelope__head .brand{position:absolute;left:12px;top:7px;width:64px}
  .envelope__head .brand__name{font-size:9px}
  .envelope__address{position:absolute;left:14px;top:34px;font-size:3.8px;color:var(--ink-light)}
</style>
</head>
<body>

  <section class="piece card card--info" aria-label="Business card, info side">
    <div class="brand"><span class="brand__dot"></span><span class="brand__name">Willow Gate Dental</span></div>
    <ul class="contact">
      <li>Celia R. Marlow, DDS</li>
      <li><span class="ico ico--round"></span>2715 Pelton Ridge Franklin, Tn 37069</li>
      <li><span class="ico"></span>willowgatedental@mailvane.com</li>
      <li><span class="ico ico--round"></span>www.willowgatedental.com</li>
      <li><span class="ico"></span>www.facebook/willowgatedental</li>
    </ul>
  </section>

  <section class="piece card card--front" aria-label="Business card, logo side">
    <div class="brand brand--lg"><span class="brand__dot"></span><span class="brand__name">Willow Gate Dental</span></div>
  </section>

  <section class="piece card card--back" aria-label="Appointment card, front">
    <div class="brand brand--sm"><span class="brand__dot"></span><span class="brand__name">Willow Gate Dental</span></div>
    <p class="doctor">Celia R. Marlow, DDS</p>
    <div class="contact">2715 Pelton Ridge Franklin, Tn 37069<br>www.willowgatedental.com</div>
  </section>

  <section class="piece card card--appointment appointment" aria-label="Appointment card, back">
    <h2>Appointment</h2>
    <div class="field">Name:<span></span></div>
    <div class="field">Date:<span></span></div>
    <div class="field">Time:<span></span></div>
  </section>

  <section class="piece letterhead" aria-label="Letterhead">
    <header class="letterhead__head">
      <div class="brand"><span class="brand__dot"></span><span class="brand__name">Willow Gate Dental</span></div>
      <ul class="contact letterhead__contact">
        <li>Celia R. Marlow, DDS</li>
        <li><span class="ico ico--round"></span>2715 Pelton Ridge Franklin, Tn 37069</li>
        <li><span class="ico"></span>willowgatedental@mailvane.com</li>
        <li><span class="ico ico--round"></span>www.willowgatedental.com</li>
        <li><span class="ico"></span>www.facebook/willowgatedental</li>
      </ul>
    </header>
    <footer class="letterhead__foot"></footer>
  </section>

  <section class="piece envelope" aria-label="Envelope">
    <header class="envelope__head">
      <div class="brand"><span class="brand__dot"></span><span class="brand__name">Willow Gate Dental</span></div>
      <p class="envelope__address">2715 Pelton Ridge Franklin, Tn 37069</p>
    </header>
  </section>

</body>
</html>
```